New Business Card

We need to refresh our business cards. We designed these ourselves and we have no graphic design experience. We would like to find a new business card design that is professional and unique. We are an auto finance company. Feel free to play with the logo, but we would like to keep the eye very present on the card. Our corporate colors are green, grey, and white.
Green - RGB - 168,215,27; HEX - #AADD22
Grey - RGB - 196,196,196; HEX - #C4C4C4
Updates
Need to upload the vector file to finalize the project. The last logo was for a jpeg that didn't stretch well.
Industry/Entity Type
Financial Service
Contact Information for Business Card
Honestly don't know...I need your help!

```html
<!DOCTYPE html>
<html lang="en">
<head>
<meta charset="utf-8">
<title>Keenview Capital – Business Card</title>
<link href="https://fonts.googleapis.com/css2?family=Pathway+Gothic+One&display=swap" rel="stylesheet">
<style>
  :root {
    --brand-green: #aed23a;
    --ink: #000000;
    --paper: #ffffff;
    --backdrop: #6b6b6b;
  }
  * { margin: 0; padding: 0; box-sizing: border-box; }
  html, body { width: 1200px; height: 900px; overflow: hidden; }
  body {
    position: relative;
    background: var(--backdrop);
    font-family: "Pathway Gothic One", "Arial Narrow", sans-serif;
  }
  .card { position: absolute; width: 602px; height: 342px; overflow: hidden; }

  /* Front */
  .card-front { left: 317px; top: 76px; background: var(--brand-green); }
  .card-front .edge-band {
    position: absolute; right: 0; top: 0; width: 39px; height: 100%; background: var(--ink);
  }
  .card-front .brand-name {
    position: absolute; left: 0; top: 0; width: 563px; height: 100%;
    display: flex; align-items: center; justify-content: center;
    color: var(--paper); font-size: 64px; letter-spacing: 1px;
  }

  /* Back */
  .card-back { left: 319px; top: 496px; width: 600px; background: var(--ink); }
  .card-back .info-panel {
    position: absolute; left: 0; top: 0; width: 202px; height: 100%; background: var(--brand-green);
  }
  .name-tab {
    position: absolute; left: 0; top: 129px; width: 47px; height: 19px; background: var(--ink);
  }
  .name-tab .dot {
    position: absolute; left: 26px; top: 4px; width: 11px; height: 11px;
    border-radius: 50%; background: var(--paper);
  }
  .holder-name {
    position: absolute; left: 54px; top: 126px; font-size: 22px; line-height: 1; color: var(--ink);
  }
  .holder-role {
    position: absolute; left: 54px; top: 150px; font-size: 15px; line-height: 1; color: var(--ink);
  }
  .contact-list { position: absolute; left: 21px; top: 211px; list-style: none; }
  .contact-list li {
    display: flex; align-items: flex-start; gap: 7px;
    font-size: 14px; line-height: 13px; color: var(--ink); margin-bottom: 5px;
  }
  .contact-list li:first-child { margin-bottom: 8px; }
  .contact-list .icon {
    flex: none; width: 26px; height: 19px; background: var(--ink);
    display: flex; align-items: center; justify-content: center;
  }
  .contact-list .text { padding-top: 3px; }
  .card-back .brand-name {
    position: absolute; left: 202px; top: 0; width: 398px; height: 100%;
    display: flex; align-items: center; justify-content: center;
    color: var(--brand-green); font-size: 30px; letter-spacing: 0.5px;
  }
</style>
</head>
<body>
  <section class="card card-front">
    <div class="brand-name">Keenview Capital</div>
    <div class="edge-band"></div>
  </section>

  <section class="card card-back">
    <div class="info-panel">
      <div class="name-tab"><span class="dot"></span></div>
      <div class="holder-name">Your Name Here</div>
      <div class="holder-role">Co-Founder &amp; CEO</div>
      <ul class="contact-list">
        <li>
          <span class="icon">
            <svg width="10" height="14" viewBox="0 0 10 14"><path d="M5 0a5 5 0 0 1 5 5c0 3.5-5 9-5 9S0 8.5 0 5a5 5 0 0 1 5-5z" fill="#fff"/><circle cx="5" cy="5" r="2" fill="#000"/></svg>
          </span>
          <span class="text">382 YOUR address<br>your City, your Country</span>
        </li>
        <li>
          <span class="icon">
            <svg width="8" height="14" viewBox="0 0 8 14"><rect x="0.75" y="0.75" width="6.5" height="12.5" rx="1" fill="none" stroke="#fff" stroke-width="1.5"/><rect x="2" y="2.5" width="4" height="7" fill="#fff"/></svg>
          </span>
          <span class="text">(007) 666-1234</span>
        </li>
        <li>
          <span class="icon">
            <svg width="16" height="11" viewBox="0 0 16 11"><rect x="0.5" y="0.5" width="15" height="10" fill="none" stroke="#fff"/><path d="M0.5 0.5 8 6.5 15.5 0.5" fill="none" stroke="#fff"/></svg>
          </span>
          <span class="text">youremail@address.com</span>
        </li>
        <li>
          <span class="icon">
            <svg width="14" height="14" viewBox="0 0 14 14" fill="none" stroke="#fff" stroke-width="1"><circle cx="7" cy="7" r="6"/><ellipse cx="7" cy="7" rx="2.6" ry="6"/><path d="M1 7h12M2 3.8h10M2 10.2h10"/></svg>
          </span>
          <span class="text">yourwebsite.com</span>
        </li>
      </ul>
    </div>
    <div class="brand-name">Keenview Capital</div>
  </section>
</body>
</html>
```